Virtual Assistant/Online Marketing Business Card/Stationary

I need a professional but modern business card/stationary for my company in Dallas called BrivoLane. BrivoLane is a virtual assistant specializing in online marketing. I would like a unique design that stands out and makes my brand clear. Incorporating the logo is a must and have attached it to this brief.

Target Market(s)

small business owners & entrepreneurs, 35-65

Industry/Entity Type

Business

Contact Information for Business Card

Dorla Finch
dorlafinch@brivolane.biz
(214) 555-0187
brivolane.biz

Font styles to use
Sans Serif

Colors
f04a50
3176b5
9bcb3c

Requirements
Must have
• Colors that match the logo colors. Logo integration

```html
<!DOCTYPE html>
<html lang="en">
<head>
<meta charset="utf-8">
<title>BrivoLane Business Card</title>
<link rel="stylesheet" href="https://fonts.googleapis.com/css2?family=Open+Sans:wght@400;600;700&family=Kalam:wght@400&display=swap">
<style>
  :root {
    --backdrop: #9b9c9c;
    --card-light: #e9e9ec;
    --card-dark: #232323;
    --ink: #222222;
    --ink-soft: #3a3a3a;
    --paper-text: #e6e6ea;
    --brand-green: #6db33f;
    --brand-red: #c0392b;
    --brand-teal: #2e9aa5;
  }
  * { margin: 0; padding: 0; box-sizing: border-box; }
  html, body {
    width: 1105px;
    height: 1200px;
    overflow: hidden;
    background: var(--backdrop);
  }
  .sheet {
    position: relative;
    width: 1105px;
    height: 1200px;
  }
  .card {
    position: absolute;
    left: 182px;
    width: 746px;
    height: 427px;
  }
  .card--front {
    top: 119px;
    background: var(--card-light);
  }
  .card--back {
    top: 635px;
    background: var(--card-dark);
  }
  .wordmark {
    position: absolute;
    left: 0;
    right: 0;
    text-align: center;
    font-family: "Open Sans", sans-serif;
    font-weight: 700;
    letter-spacing: -1px;
    line-height: 1;
  }
  .card--front .wordmark {
    top: 145px;
    font-size: 74px;
    color: var(--ink);
  }
  .card--back .wordmark {
    top: 180px;
    font-size: 92px;
    color: var(--paper-text);
  }
  .name-row {
    position: absolute;
    top: 305px;
    left: 66px;
    right: 66px;
    display: flex;
    align-items: center;
    gap: 18px;
  }
  .name-row .rule {
    flex: 1;
    height: 1.5px;
    background: var(--ink-soft);
  }
  .name {
    font-family: "Open Sans", sans-serif;
    font-weight: 600;
    font-size: 27px;
    color: var(--ink);
  }
  .contacts {
    position: absolute;
    top: 352px;
    left: 0;
    right: 0;
    display: flex;
    justify-content: center;
    gap: 22px;
    font-family: "Open Sans", sans-serif;
    font-size: 19px;
    color: var(--ink-soft);
  }
  .contact {
    display: flex;
    align-items: center;
    gap: 6px;
  }
  .contact svg { width: 18px; height: 18px; }
  .color-bands {
    position: absolute;
    left: 0;
    right: 0;
    bottom: 0;
    height: 15px;
    display: flex;
    gap: 4px;
  }
  .band { flex: 1; }
  .band--green { background: var(--brand-green); }
  .band--red { background: var(--brand-red); }
  .band--teal { background: var(--brand-teal); }
  .tagline {
    position: absolute;
    top: 358px;
    left: 0;
    right: 0;
    display: flex;
    justify-content: center;
    gap: 30px;
    font-family: "Kalam", cursive;
    font-size: 25px;
    color: var(--paper-text);
  }
  .tagline span::before {
    content: "\2022";
    margin-right: 10px;
    font-size: 22px;
  }
</style>
</head>
<body>
<main class="sheet">
  <section class="card card--front">
    <div class="wordmark">BrivoLane</div>
    <div class="name-row">
      <span class="rule"></span>
      <span class="name">Dorla Finch</span>
      <span class="rule"></span>
    </div>
    <div class="contacts">
      <span class="contact">
        <svg viewBox="0 0 18 18" aria-hidden="true"><circle cx="9" cy="9" r="9" fill="#2a2a2a"/><path d="M6 4.5l1.6 0 .7 2.3-1 .8c.6 1.3 1.5 2.2 2.8 2.8l.8-1 2.3.7 0 1.6c-4 .4-7.6-3.2-7.2-7.2z" fill="#e9e9ec"/></svg>
        (214) 555-0187
      </span>
      <span class="contact">
        <svg viewBox="0 0 18 18" aria-hidden="true"><circle cx="9" cy="9" r="9" fill="#2a2a2a"/><rect x="4" y="5.5" width="10" height="7" fill="#e9e9ec"/><path d="M4 5.5l5 4 5-4" stroke="#2a2a2a" stroke-width="1.2" fill="none"/></svg>
        dorlafinch@brivolane.biz
      </span>
      <span class="contact">
        <svg viewBox="0 0 18 18" aria-hidden="true"><circle cx="9" cy="9" r="9" fill="#2a2a2a"/><circle cx="9" cy="9" r="5" fill="none" stroke="#e9e9ec" stroke-width="1.3"/><path d="M4 9h10M9 4c-2.5 3-2.5 7 0 10M9 4c2.5 3 2.5 7 0 10" stroke="#e9e9ec" stroke-width="1" fill="none"/></svg>
        brivolane.biz
      </span>
    </div>
    <div class="color-bands">
      <span class="band band--green"></span>
      <span class="band band--red"></span>
      <span class="band band--teal"></span>
    </div>
  </section>

  <section class="card card--back">
    <div class="wordmark">BrivoLane</div>
    <div class="tagline">
      <span>Growing</span>
      <span>Brands</span>
      <span>Remotely</span>
    </div>
  </section>
</main>
</body>
</html>
```